" A proposta da empresa foca em Saúde e bem-estar > Odontologia estética: prótese, restauraçao e estética. Trata-se de uma nova proposta de atendimento de saúde oferecendo bem-estar através dos mais modernos tratamentos odontológicos de alto valor agregado, visando elevada satisfaçao das pessoas com resultados estéticos de alto nível. Nossos produtos e serviços sao produtos de saúde e bem-estar odontologia é o "meio" que oferecemos. A marca é o próprio profissional uma vez que serao dois locais de atendimento (dois endereços) com segmentaçao diferenciada. Um onde somente serao atendidos os públicos Classes AA e A. E outro para as classes A e B. "

```html
<!DOCTYPE html>
<html lang="pt-BR">
<head>
<meta charset="UTF-8">
<title>Dra. Helena Vasconi — Cartões de visita</title>
<link rel="stylesheet" href="https://fonts.googleapis.com/css2?family=Cinzel:wght@400;500&family=Cormorant+Garamond:wght@400;500;600&display=swap">
<style>
  :root {
    --page: #ecebe7;
    --black: #0a0a0a;
    --ink: #141414;
    --gold-light: #e9d9a6;
    --gold: #c2a25a;
    --gold-mid: #a98a44;
    --gold-deep: #7a6128;
    --brown: #5a4519;
    --cream: #f3ecd8;
  }
  * { box-sizing: border-box; margin: 0; padding: 0; }
  html, body { width: 1200px; height: 1200px; overflow: hidden; }
  body {
    background: var(--page);
    font-family: "Cormorant Garamond", Georgia, serif;
    position: relative;
  }

  .card {
    position: absolute;
    left: 150px;
    width: 900px;
    height: 500px;
    overflow: hidden;
    box-shadow: 0 14px 30px rgba(0,0,0,.22);
  }

  /* Front: black card */
  .card--front {
    top: 70px;
    background: var(--black);
  }
  .card--front .trim {
    position: absolute;
    left: 0; right: 0;
    height: 26px;
    background: linear-gradient(90deg, var(--gold-deep), var(--gold-light) 35%, var(--gold) 60%, var(--gold-deep));
  }
  .card--front .trim--top { top: 0; }
  .card--front .trim--bottom { bottom: 0; }
  .card--front .trim::after {
    content: "";
    position: absolute;
    left: 0; right: 0;
    height: 6px;
    background: var(--black);
  }
  .card--front .trim--top::after { bottom: 8px; }
  .card--front .trim--bottom::after { top: 8px; }

  .front-mark {
    position: absolute;
    left: 310px;
    top: 120px;
    width: 230px;
    height: 230px;
    border-radius: 50%;
    border: 10px solid var(--gold);
  }
  .front-initials {
    position: absolute;
    left: 610px;
    top: 300px;
    font-size: 64px;
    font-weight: 500;
    letter-spacing: 4px;
    color: var(--gold);
  }

  /* Back: gold card */
  .card--back {
    top: 630px;
    background: linear-gradient(115deg, var(--gold-deep) 0%, var(--gold) 22%, var(--gold-light) 45%, var(--gold) 62%, var(--gold-mid) 80%, var(--gold-deep) 100%);
  }
  .back-mark {
    position: absolute;
    left: 408px;
    top: 58px;
    width: 84px;
    height: 84px;
    border-radius: 50%;
    border: 6px solid var(--brown);
  }
  .back-name {
    position: absolute;
    left: 0; right: 0;
    top: 150px;
    text-align: center;
    font-size: 70px;
    font-weight: 500;
    line-height: 1.1;
    color: var(--brown);
  }
  .back-specialty {
    position: absolute;
    left: 0; right: 0;
    top: 258px;
    text-align: center;
    font-family: "Cinzel", "Times New Roman", serif;
    font-size: 21px;
    letter-spacing: 5px;
    color: var(--brown);
  }
  .contact-band {
    position: absolute;
    left: 0; right: 0; bottom: 0;
    height: 140px;
    background: var(--ink);
    border-top: 4px solid var(--gold-deep);
    color: var(--cream);
    display: flex;
    flex-direction: column;
    justify-content: center;
    align-items: center;
    gap: 10px;
    font-size: 21px;
    font-weight: 500;
    white-space: nowrap;
  }
</style>
</head>
<body>
  <section class="card card--front" aria-label="Frente do cartão">
    <div class="trim trim--top"></div>
    <div class="front-mark"></div>
    <div class="front-initials">HV</div>
    <div class="trim trim--bottom"></div>
  </section>

  <section class="card card--back" aria-label="Verso do cartão">
    <div class="back-mark"></div>
    <h1 class="back-name">Dra. Helena Vasconi</h1>
    <p class="back-specialty">ODONTOLOGIA E ESTÉTICA</p>
    <div class="contact-band">
      <p class="contact-line">Av. das Palmeiras, 2480 | Jardins | SP | CEP 01420-030 | Cel: 11 9342 5718 | Tel: 11 3856 2094</p>
      <p class="contact-line">helena@helenavasconi.com.br | www.helenavasconi.com.br</p>
    </div>
  </section>
</body>
</html>
```